Marlowe Sail Works President Business Card Carbon fiber catamarans

Hi.. I need a new business card design.. I am the President of a high tech yacht builder. We build Carbon Fiber go fast catamarans... Maybe we use the file I am sharing to you as the back of the card.. We need to look cool and crisp ...

Target Market(s)

Affluent People who will purchase a cool yacht

Industry/Entity Type

Custom Yacht Builder

Contact Information for Business Card

Dean Pellington , President, 512.608.3419 USA

Font styles to use
Serif

Requirements
Must have
• the clean crisp cool feel
Nice to have
• clean and crisp
Should not have
• Bold ugly

```html
<!DOCTYPE html>
<html lang="en">
<head>
<meta charset="utf-8">
<title>Marlowe Sail Works — Business Card</title>
<link href="https://fonts.googleapis.com/css2?family=Exo+2:wght@300;400&display=swap" rel="stylesheet">
<style>
  :root {
    --stage: #2b2b2d;
    --carbon-dark: #141416;
    --carbon-light: #2c2c30;
    --card-top: #3a3a3d;
    --card-bottom: #1e1e20;
    --silver: #e6e6e8;
    --silver-soft: #bdbdc1;
    --muted: #9a9a9f;
  }
  * { box-sizing: border-box; margin: 0; padding: 0; }
  html, body { width: 1200px; height: 874px; overflow: hidden; background: var(--stage); }
  body { font-family: "Exo 2", sans-serif; font-weight: 300; color: var(--silver); }
  .canvas { position: relative; width: 1200px; height: 874px; }

  .card {
    position: absolute; left: 300px; width: 600px; height: 340px;
    border-radius: 4px; overflow: hidden;
    box-shadow: 0 10px 30px rgba(0,0,0,.45);
  }
  .card--front { top: 80px; }
  .card--back { top: 454px;
    background: linear-gradient(160deg, var(--card-top), var(--card-bottom)); }

  .carbon-texture {
    position: absolute; inset: 0;
    background: radial-gradient(ellipse at 45% 35%, var(--carbon-light), var(--carbon-dark) 75%);
  }
  .front-wordmark {
    position: absolute; left: 0; right: 0; top: 128px;
    display: flex; align-items: center; justify-content: center; gap: 18px;
  }
  .front-wordmark .mark-square { width: 40px; height: 40px; background: var(--silver); }
  .front-wordmark .brand-name {
    font-size: 44px; letter-spacing: 5px; text-transform: uppercase; color: var(--silver);
  }

  .contact { position: absolute; left: 44px; top: 36px; }
  .contact .person-name { font-size: 24px; letter-spacing: 1.5px; text-transform: uppercase; }
  .contact .person-role { font-size: 14px; color: var(--muted); margin-bottom: 26px; }
  .contact .address { font-size: 15px; line-height: 1.3; color: var(--silver-soft); margin-bottom: 12px; }
  .contact ul { list-style: none; }
  .contact li { display: flex; align-items: center; gap: 10px; font-size: 15px; line-height: 1.45; color: var(--silver-soft); }
  .contact li svg { width: 13px; height: 13px; fill: var(--silver-soft); flex: none; }

  .back-wordmark {
    position: absolute; right: 40px; top: 120px; width: 220px;
    display: flex; align-items: center; gap: 12px;
  }
  .back-wordmark .mark-square { width: 28px; height: 28px; background: var(--silver-soft); flex: none; }
  .back-wordmark .brand-name { font-size: 24px; line-height: 1.15; letter-spacing: 2px; text-transform: uppercase; color: var(--silver-soft); }
</style>
</head>
<body>
<main class="canvas">
  <section class="card card--front">
    <div class="carbon-texture" role="img" aria-label="Woven carbon fiber texture"></div>
    <div class="front-wordmark">
      <span class="mark-square"></span>
      <span class="brand-name">Marlowe Sail Works</span>
    </div>
  </section>

  <section class="card card--back">
    <div class="contact">
      <h1 class="person-name">Dean Pellington</h1>
      <p class="person-role">President</p>
      <p class="address">2140 Harbor Point Road<br>Newport<br>Rhode Island 02840</p>
      <ul>
        <li><svg viewBox="0 0 16 16"><path d="M3 1l3 3-2 2c1 2 3 4 6 6l2-2 3 3-2 3C7 16 0 9 0 4z"/></svg>512.608.3419</li>
        <li><svg viewBox="0 0 16 16"><path d="M4 0h8v16H4zM5 2v10h6V2z"/></svg>512.608.3420</li>
        <li><svg viewBox="0 0 16 16"><path d="M4 1h8v4H4zM1 6h14v7h-3v2H4v-2H1zM5 10v4h6v-4z"/></svg>512.608.3421</li>
        <li><svg viewBox="0 0 16 16"><path d="M0 3h16v10H0zM1 4l7 5 7-5z"/></svg>name@marlowesail.com</li>
        <li><svg viewBox="0 0 16 16"><circle cx="8" cy="8" r="7"/></svg>www.marlowesail.com</li>
      </ul>
    </div>
    <div class="back-wordmark">
      <span class="mark-square"></span>
      <span class="brand-name">Marlowe Sail Works</span>
    </div>
  </section>
</main>
</body>
</html>
```